Engineering/Manufacturing Company Needs PowerPoint Update and Template

We want to update the look and feel of our current corporate overview PowerPoint. We would like a working template moving forward with 6-8 slide layouts as well as a couple cover page options. Our content ranges from basic bullet points to complex graphs, images, and a combination of those, so we need templates that will work with a wide variety of content.
Our company specializes in complex precision machining, Engineering, and Advanced heavy duty truck products. We would like this presentation to represent our high-level manufacturing technology.
Our corporate color is blue (RBG 26/75/159), and we also use gray and white. We are looking for a modern, clean, yet masculine/industrial feeling. I have included our company logo, but other than that we would like to see what you can come up with. We would like it to feel clean yet industrial.
Target Market(s)
High-level management in the manufacturing and heavy duty truck/bus industries.
Industry/Entity Type
Manufacturer

```html
<!DOCTYPE html>
<html lang="en">
<head>
<meta charset="utf-8">
<title>Korvex Corporate Template Sheet</title>
<link href="https://fonts.googleapis.com/css2?family=Oswald:wght@400;500;700&family=Open+Sans:wght@400;600;700&family=Roboto:wght@400;500;700&display=swap" rel="stylesheet">
<style>
  :root{
    --brand-blue:#1a4b9f;
    --bright-blue:#1e5fd6;
    --steel-gray:#7f7f7f;
    --sheet-bg:#a9a9a9;
    --white:#ffffff;
    --ink:#1b1b1b;
    --muted:#8a8a8a;
    --disc:#ececec;
    --card-1:#ababab;
    --card-2:#949494;
    --card-3:#7a7a7a;
  }
  html,body{margin:0;padding:0;overflow:hidden;}
  body{width:1200px;height:1200px;background:var(--sheet-bg);position:relative;font-family:"Open Sans",sans-serif;}
  .slide{position:absolute;width:553px;height:311px;display:block;box-shadow:0 1px 3px rgba(0,0,0,.25);}
  .slide--cover{left:29px;top:50px;}
  .slide--agenda{left:621px;top:50px;}
  .slide--process{left:29px;top:425px;}
  .slide--pillars{left:621px;top:425px;}
  .slide--stats{left:324px;top:809px;}
  .caption{position:absolute;width:553px;text-align:center;font-family:"Roboto",sans-serif;font-size:16.5px;color:#222;letter-spacing:.3px;}
  .caption--cover{left:29px;top:378px;}
  .caption--agenda{left:621px;top:378px;}
  .caption--process{left:29px;top:754px;}
  .caption--pillars{left:621px;top:754px;}
  .caption--stats{left:324px;top:1138px;}

  .fill-blue{fill:var(--brand-blue);}
  .fill-gray{fill:var(--steel-gray);}
  .fill-white{fill:var(--white);}
  .brand{font-family:"Oswald",sans-serif;font-weight:700;fill:var(--brand-blue);letter-spacing:1px;}
  .hero-title{font-family:"Oswald",sans-serif;font-weight:400;font-size:46px;fill:var(--white);}
  .hero-sub{font-family:"Open Sans",sans-serif;font-size:10.5px;fill:var(--white);}
  .web{font-family:"Open Sans",sans-serif;font-size:9.5px;letter-spacing:2px;fill:var(--brand-blue);}
  .list-num{font-family:"Open Sans",sans-serif;font-size:12px;fill:var(--brand-blue);}
  .list-text{font-family:"Open Sans",sans-serif;font-size:12px;fill:#333;}
  .head-blue{font-family:"Oswald",sans-serif;font-weight:500;font-size:20px;fill:var(--brand-blue);}
  .head-dark{font-family:"Oswald",sans-serif;font-weight:500;font-size:20px;fill:var(--ink);}
  .step-label{font-family:"Roboto",sans-serif;font-weight:700;font-size:8.5px;fill:var(--brand-blue);}
  .step-text{font-family:"Open Sans",sans-serif;font-size:7.5px;fill:var(--muted);}
  .card-text{font-family:"Open Sans",sans-serif;font-size:8.5px;fill:var(--white);}
  .page-num{font-family:"Roboto",sans-serif;font-weight:700;font-size:9px;fill:var(--white);}
  .stat-num{font-family:"Roboto",sans-serif;font-weight:700;font-size:21px;fill:var(--ink);}
  .stat-title{font-family:"Open Sans",sans-serif;font-size:11px;fill:var(--ink);}
  .stat-text{font-family:"Open Sans",sans-serif;font-size:7px;fill:#333;}
  .rule{stroke:var(--brand-blue);stroke-width:1;}
  .connector{fill:none;stroke:#222;stroke-width:1;}
</style>
</head>
<body>

<!-- Cover -->
<svg class="slide slide--cover" viewBox="0 0 691 389" xmlns="http://www.w3.org/2000/svg">
  <rect width="691" height="389" class="fill-white"/>
  <polygon points="420,0 691,0 691,389 420,389 310,195" fill="#6f6a5f" role="img" aria-label="Overhead photo of engineers reviewing technical drawings at a table"/>
  <polygon points="372,0 420,0 310,195 262,195" class="fill-gray"/>
  <polygon points="262,195 310,195 420,389 372,389" class="fill-blue"/>
  <polygon points="0,197 265,197 330,318 0,318" class="fill-blue"/>
  <text x="46" y="118" class="brand" font-size="60">KORVEX</text>
  <text x="20" y="250" class="hero-title">LOREM IPSUM</text>
  <rect x="20" y="256" width="112" height="2" class="fill-white"/>
  <text x="20" y="285" class="hero-sub">SIMPLY DUMMY TEXT OF THE PRINTING AND</text>
  <text x="20" y="301" class="hero-sub">TYPESETTING INDUSTRY</text>
  <line x1="0" y1="363" x2="160" y2="363" class="rule"/>
  <g transform="translate(172,363)" fill="none" stroke="var(--brand-blue)" stroke-width=".9"><circle r="4"/><ellipse rx="1.8" ry="4"/><line x1="-4" x2="4"/></g>
  <text x="183" y="366.5" class="web">www.websiteaddress.com</text>
</svg>
<div class="caption caption--cover">COVER PAGE</div>

<!-- Agenda list -->
<svg class="slide slide--agenda" viewBox="0 0 691 389" xmlns="http://www.w3.org/2000/svg">
  <rect width="691" height="389" class="fill-white"/>
  <polygon points="0,0 374,0 264,195 374,389 0,389" fill="#9fb7b4" role="img" aria-label="Photo of a hand sketching notes beside a laptop keyboard"/>
  <polygon points="374,0 424,0 314,195 264,195" class="fill-gray"/>
  <polygon points="264,195 314,195 424,389 374,389" class="fill-blue"/>
  <text x="528" y="58" class="brand" font-size="40">KORVEX</text>
  <g>
    <text x="420" y="132" class="list-num">1.</text><text x="440" y="132" class="list-text">Lorem Ipsum is simply dummy.</text>
    <text x="420" y="163" class="list-num">2.</text><text x="440" y="163" class="list-text">The printing and typesetting industry.</text>
    <text x="420" y="194" class="list-num">3.</text><text x="440" y="194" class="list-text">Lorem Ipsum has been the industry's.</text>
    <text x="420" y="225" class="list-num">4.</text><text x="440" y="225" class="list-text">Standard dummy text ever since.</text>
    <text x="420" y="256" class="list-num">5.</text><text x="440" y="256" class="list-text">Lorem Ipsum is simply dummy.</text>
    <text x="420" y="287" class="list-num">6.</text><text x="440" y="287" class="list-text">The printing and typesetting industry.</text>
  </g>
  <line x1="410" y1="363" x2="488" y2="363" class="rule"/>
  <g transform="translate(499,363)" fill="none" stroke="var(--brand-blue)" stroke-width=".9"><circle r="4"/><ellipse rx="1.8" ry="4"/><line x1="-4" x2="4"/></g>
  <text x="510" y="366.5" class="web">www.websiteaddress.com</text>
</svg>
<div class="caption caption--agenda">INNER PAGE 01</div>

<!-- Process steps -->
<svg class="slide slide--process" viewBox="0 0 691 389" xmlns="http://www.w3.org/2000/svg">
  <defs>
    <radialGradient id="disc-glow" cx="50%" cy="35%" r="65%"><stop offset="0" stop-color="#f7f7f7"/><stop offset="1" stop-color="#e4e4e4"/></radialGradient>
  </defs>
  <rect width="691" height="389" class="fill-white"/>
  <text x="20" y="37"><tspan class="head-blue">LOREM IPSUM</tspan><tspan class="head-dark"> IS SIMPLY DUMMY</tspan></text>
  <rect x="20" y="45" width="110" height="2" class="fill-blue"/>
  <polygon points="621,0 667,0 560,194 511,194" class="fill-gray"/>
  <polygon points="511,194 560,194 667,389 621,389" class="fill-blue"/>
  <text x="578" y="211" class="brand" font-size="27">KORVEX</text>
  <text x="629" y="366" class="page-num">02</text>

  <circle cx="244" cy="200" r="88" fill="url(#disc-glow)"/>
  <circle cx="244" cy="200" r="68" fill="#f2f2f2" stroke="#fff" stroke-width="3"/>
  <text x="244" y="209" class="brand" font-size="25" text-anchor="middle">KORVEX</text>

  <text x="133" y="116" class="step-label" text-anchor="end">STEP 01</text>
  <text x="133" y="129" class="step-text" text-anchor="end">Lorem Ipsum is simply</text>
  <text x="133" y="141" class="step-text" text-anchor="end">dummy text of the.</text>
  <path d="M139 113 H186 V137 H195" class="connector"/>
  <text x="133" y="194" class="step-label" text-anchor="end">STEP 02</text>
  <text x="133" y="207" class="step-text" text-anchor="end">Lorem Ipsum is simply</text>
  <text x="133" y="219" class="step-text" text-anchor="end">dummy text of the.</text>
  <path d="M139 191 H152" class="connector"/>
  <text x="133" y="274" class="step-label" text-anchor="end">STEP 03</text>
  <text x="133" y="286" class="step-text" text-anchor="end">Lorem Ipsum is simply</text>
  <text x="133" y="298" class="step-text" text-anchor="end">dummy text of the.</text>
  <path d="M139 271 H174 V246 H180" class="connector"/>

  <text x="354" y="116" class="step-label">STEP 04</text>
  <text x="354" y="129" class="step-text">Lorem Ipsum is simply</text>
  <text x="354" y="141" class="step-text">dummy text of the.</text>
  <path d="M348 113 H301 V137 H295" class="connector"/>
  <text x="354" y="194" class="step-label">STEP 05</text>
  <text x="354" y="207" class="step-text">Lorem Ipsum is simply</text>
  <text x="354" y="219" class="step-text">dummy text of the.</text>
  <path d="M348 191 H334" class="connector"/>
  <text x="354" y="273" class="step-label">STEP 06</text>
  <text x="354" y="286" class="step-text">Lorem Ipsum is simply</text>
  <text x="354" y="298" class="step-text">dummy text of the.</text>
  <path d="M348 270 H313 V245 H307" class="connector"/>

  <line x1="0" y1="363" x2="245" y2="363" class="rule"/>
  <g transform="translate(257,363)" fill="none" stroke="var(--brand-blue)" stroke-width=".9"><circle r="4"/><ellipse rx="1.8" ry="4"/><line x1="-4" x2="4"/></g>
  <text x="267" y="366.5" class="web">www.websiteaddress.com</text>
</svg>
<div class="caption caption--process">INNER PAGE 02</div>

<!-- Three pillars -->
<svg class="slide slide--pillars" viewBox="0 0 691 389" xmlns="http://www.w3.org/2000/svg">
  <rect width="691" height="389" class="fill-white"/>
  <text x="20" y="37"><tspan class="head-blue">LOREM IPSUM</tspan><tspan class="head-dark"> IS SIMPLY DUMMY</tspan></text>
  <rect x="20" y="45" width="110" height="2" class="fill-blue"/>
  <polygon points="621,0 667,0 560,194 511,194" class="fill-gray"/>
  <polygon points="511,194 560,194 667,389 621,389" class="fill-blue"/>
  <text x="578" y="211" class="brand" font-size="27">KORVEX</text>
  <text x="629" y="366" class="page-num">03</text>

  <g class="pillar">
    <polygon points="64,82 180,82 180,244 122,317 64,244" fill="var(--card-1)"/>
    <text x="122" y="108" class="card-text" text-anchor="middle">Lorem Ipsum is simply</text>
    <line x1="74" y1="120" x2="170" y2="120" stroke="#c4c4c4" stroke-width=".6"/>
    <text x="122" y="137" class="card-text" text-anchor="middle">Lorem Ipsum is simply</text>
    <line x1="74" y1="149" x2="170" y2="149" stroke="#c4c4c4" stroke-width=".6"/>
    <text x="122" y="166" class="card-text" text-anchor="middle">Lorem Ipsum is simply</text>
    <line x1="74" y1="178" x2="170" y2="178" stroke="#c4c4c4" stroke-width=".6"/>
    <text x="122" y="195" class="card-text" text-anchor="middle">Lorem Ipsum is simply</text>
    <polygon points="122,218 170,262 122,306 74,262" class="fill-white"/>
    <g fill="none" stroke="var(--card-1)" stroke-width="3"><circle cx="116" cy="256" r="7" stroke-dasharray="3 2"/><circle cx="130" cy="270" r="5" stroke-dasharray="2.5 1.5"/></g>
  </g>
  <g class="pillar">
    <polygon points="196,82 313,82 313,244 254.5,317 196,244" fill="var(--card-2)"/>
    <text x="254.5" y="108" class="card-text" text-anchor="middle">Lorem Ipsum is simply</text>
    <line x1="206" y1="120" x2="303" y2="120" stroke="#b0b0b0" stroke-width=".6"/>
    <text x="254.5" y="137" class="card-text" text-anchor="middle">Lorem Ipsum is simply</text>
    <line x1="206" y1="149" x2="303" y2="149" stroke="#b0b0b0" stroke-width=".6"/>
    <text x="254.5" y="166" class="card-text" text-anchor="middle">Lorem Ipsum is simply</text>
    <line x1="206" y1="178" x2="303" y2="178" stroke="#b0b0b0" stroke-width=".6"/>
    <text x="254.5" y="195" class="card-text" text-anchor="middle">Lorem Ipsum is simply</text>
    <polygon points="254.5,218 302.5,262 254.5,306 206.5,262" class="fill-white"/>
    <rect x="244" y="252" width="21" height="21" rx="3" fill="#555"/>
  </g>
  <g class="pillar">
    <polygon points="329,82 446,82 446,244 387.5,317 329,244" fill="var(--card-3)"/>
    <text x="387.5" y="108" class="card-text" text-anchor="middle">Lorem Ipsum is simply</text>
    <line x1="339" y1="120" x2="436" y2="120" stroke="#9a9a9a" stroke-width=".6"/>
    <text x="387.5" y="137" class="card-text" text-anchor="middle">Lorem Ipsum is simply</text>
    <line x1="339" y1="149" x2="436" y2="149" stroke="#9a9a9a" stroke-width=".6"/>
    <text x="387.5" y="166" class="card-text" text-anchor="middle">Lorem Ipsum is simply</text>
    <line x1="339" y1="178" x2="436" y2="178" stroke="#9a9a9a" stroke-width=".6"/>
    <text x="387.5" y="195" class="card-text" text-anchor="middle">Lorem Ipsum is simply</text>
    <polygon points="387.5,218 435.5,262 387.5,306 339.5,262" class="fill-white"/>
    <circle cx="387.5" cy="262" r="11" fill="none" stroke="#555" stroke-width="2"/>
  </g>

  <line x1="0" y1="363" x2="245" y2="363" class="rule"/>
  <g transform="translate(257,363)" fill="none" stroke="var(--brand-blue)" stroke-width=".9"><circle r="4"/><ellipse rx="1.8" ry="4"/><line x1="-4" x2="4"/></g>
  <text x="267" y="366.5" class="web">www.websiteaddress.com</text>
</svg>
<div class="caption caption--pillars">INNER PAGE 03</div>

<!-- Statistics -->
<svg class="slide slide--stats" viewBox="0 0 691 389" xmlns="http://www.w3.org/2000/svg">
  <rect width="691" height="389" class="fill-white"/>
  <text x="20" y="37"><tspan class="head-blue">LOREM IPSUM</tspan><tspan class="head-dark"> IS SIMPLY DUMMY</tspan></text>
  <rect x="20" y="45" width="110" height="2" class="fill-blue"/>
  <polygon points="620,0 666,0 559,194 510,194" class="fill-gray"/>
  <polygon points="510,194 559,194 666,389 620,389" class="fill-blue"/>
  <text x="577" y="211" class="brand" font-size="27">KORVEX</text>
  <text x="623" y="366" class="page-num">04</text>

  <line x1="263" y1="122" x2="263" y2="295" stroke="#d5d5d5" stroke-width="1"/>

  <g class="gauge">
    <circle cx="69" cy="129" r="40" fill="var(--disc)"/>
    <circle cx="69" cy="129" r="45" fill="none" stroke="var(--brand-blue)" stroke-width="6" stroke-dasharray="141.4 283" transform="rotate(180 69 129)"/>
    <text x="69" y="137" class="stat-num" text-anchor="middle">50</text>
    <text x="130" y="116" class="stat-title">lorem ipsum simply</text>
    <text x="130" y="128" class="stat-text">Lorem Ipsum is simply</text>
    <text x="130" y="138.5" class="stat-text">dummy text of the printing</text>
    <text x="130" y="149" class="stat-text">and typesetting industry.</text>
  </g>
  <g class="gauge">
    <circle cx="347" cy="129" r="40" fill="var(--disc)"/>
    <circle cx="347" cy="129" r="45" fill="none" stroke="var(--bright-blue)" stroke-width="6" stroke-dasharray="198 283" transform="rotate(180 347 129)"/>
    <text x="347" y="137" class="stat-num" text-anchor="middle">70</text>
    <text x="408" y="116" class="stat-title">lorem ipsum simply</text>
    <text x="408" y="128" class="stat-text">Lorem Ipsum is simply</text>
    <text x="408" y="138.5" class="stat-text">dummy text of the printing</text>
    <text x="408" y="149" class="stat-text">and typesetting industry.</text>
  </g>
  <g class="gauge">
    <circle cx="69" cy="275" r="40" fill="var(--disc)"/>
    <circle cx="69" cy="275" r="45" fill="none" stroke="#555" stroke-width="6" stroke-dasharray="115 283" transform="rotate(185 69 275)"/>
    <text x="69" y="283" class="stat-num" text-anchor="middle">30</text>
    <text x="130" y="262" class="stat-title">lorem ipsum simply</text>
    <text x="130" y="274" class="stat-text">Lorem Ipsum is simply</text>
    <text x="130" y="284.5" class="stat-text">dummy text of the printing</text>
    <text x="130" y="295" class="stat-text">and typesetting industry.</text>
  </g>
  <g class="gauge">
    <circle cx="347" cy="275" r="40" fill="var(--disc)"/>
    <circle cx="347" cy="275" r="45" fill="none" stroke="#111" stroke-width="6" stroke-dasharray="80 283" transform="rotate(170 347 275)"/>
    <text x="347" y="283" class="stat-num" text-anchor="middle">10</text>
    <text x="408" y="262" class="stat-title">lorem ipsum simply</text>
    <text x="408" y="274" class="stat-text">Lorem Ipsum is simply</text>
    <text x="408" y="284.5" class="stat-text">dummy text of the printing</text>
    <text x="408" y="295" class="stat-text">and typesetting industry.</text>
  </g>

  <line x1="0" y1="363" x2="245" y2="363" class="rule"/>
  <g transform="translate(257,363)" fill="none" stroke="var(--brand-blue)" stroke-width=".9"><circle r="4"/><ellipse rx="1.8" ry="4"/><line x1="-4" x2="4"/></g>
  <text x="267" y="366.5" class="web">www.websiteaddress.com</text>
</svg>
<div class="caption caption--stats">INNER PAGE 04</div>

</body>
</html>
```